Dental Consulting Business Card - Stationary
Business Card / Stationary
Modern
Glen R. Castellano
President
4817 W. Harborview Ave.
Larkspur Bay, KV
glen@zuvadentalconsulting.example
www.zuvadentalconsulting.example

```html
<!DOCTYPE html>
<html lang="en">
<head>
<meta charset="utf-8">
<title>ZuvaDental Stationery</title>
<link rel="stylesheet" href="https://fonts.googleapis.com/css2?family=Open+Sans:wght@400;600;700;800&display=swap">
<style>
:root{
  --bg:#d6d8da;
  --paper:#ffffff;
  --ink:#4a4b4d;
  --ink-dark:#3d3e40;
  --muted:#8a8c8f;
  --blue:#2a8fc8;
  --green:#7ab929;
  --rule:#e3e4e6;
}
*{box-sizing:border-box;margin:0;padding:0}
html,body{width:1200px;height:790px;overflow:hidden}
body{background:var(--bg);font-family:"Open Sans",Arial,sans-serif;color:var(--ink)}
.canvas{position:relative;width:1200px;height:790px}
.sheet{position:absolute;background:var(--paper);box-shadow:0 2px 8px rgba(0,0,0,.18);overflow:hidden}

.brand{display:flex;align-items:center;gap:7px;font-weight:800;color:var(--blue);letter-spacing:-.3px;white-space:nowrap}
.brand-dot{width:14px;height:14px;border-radius:50%;background:var(--green);flex:none}
.brand--light{color:#fff}

.stripes{position:absolute;left:0;right:0;height:6px}
.stripes::before,.stripes::after{content:"";position:absolute;left:0;right:0;height:2px}
.stripes::before{top:0;background:var(--blue)}
.stripes::after{bottom:0;background:var(--green)}

/* Letterhead */
.letterhead{left:40px;top:40px;width:400px;height:560px;padding:34px 38px}
.letterhead .brand{font-size:22px}
.letterhead .greeting{margin-top:40px;font-size:15px;font-weight:600;color:var(--ink-dark)}
.letterhead .body{margin-top:14px;font-size:9.5px;line-height:1.65;color:var(--muted)}
.letterhead .body p{margin-bottom:10px}
.letterhead .closing{margin-top:12px;font-size:9.5px;color:var(--muted)}
.letterhead .sign-line{margin-top:32px;width:130px;border-top:1px solid var(--rule)}
.letterhead .signer{margin-top:6px;font-size:10px;font-weight:600;color:var(--ink)}
.letterhead .footer{position:absolute;left:0;right:0;bottom:22px}
.letterhead .footer .stripes{position:relative;margin-bottom:8px}
.letterhead .footer-text{text-align:center;font-size:8px;color:var(--muted);white-space:nowrap}

/* Envelope */
.envelope{left:470px;top:40px;width:690px;height:260px;padding:26px 30px}
.envelope .brand{font-size:20px}
.envelope .return{margin-top:8px;font-size:8.5px;line-height:1.5;color:var(--muted)}
.envelope .stripes{bottom:24px}

/* Cards */
.card{width:340px;height:195px}
.card-front-a{left:470px;top:330px}
.card-front-b{left:820px;top:330px}
.card-back-light{left:470px;top:555px}
.card-back-dark{left:820px;top:555px;background:var(--ink)}

.name-band{height:40px;background:var(--ink);display:flex;align-items:center;padding:0 18px;color:#fff;font-size:12px;font-weight:700;gap:8px}
.name-band .title{font-weight:400;font-size:10px;opacity:.85}
.name-band .bar{width:1px;height:14px;background:rgba(255,255,255,.6)}
.card-front-a .stripes{top:40px}
.card-front-a .inner{display:flex;justify-content:space-between;padding:26px 18px 0}
.card-front-a .brand{font-size:19px}
.address{font-size:8.5px;line-height:1.5;color:var(--ink)}
.contacts{padding:10px 18px 0 160px;font-size:8px;line-height:1.8;color:var(--ink)}
.contacts li{list-style:none;display:flex;align-items:center;gap:5px;white-space:nowrap}
.contacts svg{width:9px;height:9px;flex:none}

.card-front-b .top{display:flex;justify-content:space-between;align-items:flex-start;padding:22px 18px 0}
.card-front-b .brand{font-size:19px}
.card-front-b .person{text-align:right}
.card-front-b .person .name{font-size:13px;font-weight:700;color:var(--blue)}
.card-front-b .person .title{font-size:9px;color:var(--muted)}
.card-front-b .contacts{padding:12px 18px 0 160px}
.card-front-b .stripes{bottom:40px}
.card-front-b .foot-band{position:absolute;left:0;right:0;bottom:0;height:36px;background:var(--ink);color:#fff;font-size:8.5px;display:flex;align-items:center;padding:0 18px}

.card-back-light .centre,.card-back-dark .centre{height:100%;display:flex;flex-direction:column;align-items:center;justify-content:center;gap:10px}
.card-back-light .brand,.card-back-dark .brand{font-size:24px}
.tagline{font-size:9px;color:var(--muted);letter-spacing:.3px}
.card-back-dark .tagline{color:#d5d6d8}
.card-back-light .stripes{bottom:16px}
</style>
</head>
<body>
<main class="canvas">

  <section class="sheet letterhead" aria-label="Letterhead">
    <div class="brand"><span class="brand-dot"></span>ZuvaDental</div>
    <p class="greeting">Hello,</p>
    <div class="body">
      <p>Thank you for your interest in our consulting services. We help dental practices grow with clear planning, steady marketing and careful attention to every patient visit. Our team studies your office, your numbers and your goals before we suggest a single change.</p>
      <p>From front desk training to new patient campaigns, we build a plan that fits your practice and your budget. Each step is measured, reviewed and adjusted so that results stay visible month after month.</p>
      <p>We look forward to working with you and your team.</p>
    </div>
    <p class="closing">Sincerely,</p>
    <div class="sign-line"></div>
    <p class="signer">Glen R. Castellano</p>
    <div class="footer">
      <div class="stripes"></div>
      <p class="footer-text">(555) 555-0142 &nbsp;|&nbsp; 4817 W. Harborview Ave., Larkspur Bay, KV &nbsp;|&nbsp; www.zuvadentalconsulting.example</p>
    </div>
  </section>

  <section class="sheet envelope" aria-label="Envelope">
    <div class="brand"><span class="brand-dot"></span>ZuvaDental</div>
    <p class="return">4817 W. Harborview Ave.<br>Larkspur Bay, KV</p>
    <div class="stripes"></div>
  </section>

  <section class="sheet card card-front-a" aria-label="Business card front">
    <div class="name-band">Glen R. Castellano <span class="bar"></span><span class="title">President</span></div>
    <div class="stripes"></div>
    <div class="inner">
      <div class="brand"><span class="brand-dot"></span>ZuvaDental</div>
      <p class="address">4817 W. Harborview Ave.<br>Larkspur Bay, KV</p>
    </div>
    <ul class="contacts">
      <li><svg viewBox="0 0 10 10"><path d="M2 1h2l1 2-1 1a5 5 0 0 0 2 2l1-1 2 1v2a1 1 0 0 1-1 1A8 8 0 0 1 1 2a1 1 0 0 1 1-1z" fill="var(--blue)"/></svg>(555) 555-0142</li>
      <li><svg viewBox="0 0 10 10"><rect x="0.5" y="2" width="9" height="6" fill="none" stroke="var(--blue)"/><path d="M.5 2 5 5.5 9.5 2" fill="none" stroke="var(--blue)"/></svg>glen@zuvadentalconsulting.example</li>
      <li><svg viewBox="0 0 10 10"><circle cx="5" cy="5" r="4.2" fill="none" stroke="var(--blue)"/><path d="M1 5h8M5 .8c2 2.5 2 5.9 0 8.4M5 .8c-2 2.5-2 5.9 0 8.4" fill="none" stroke="var(--blue)" stroke-width=".8"/></svg>www.zuvadentalconsulting.example</li>
    </ul>
  </section>

  <section class="sheet card card-front-b" aria-label="Business card front, alternate">
    <div class="top">
      <div class="brand"><span class="brand-dot"></span>ZuvaDental</div>
      <div class="person"><p class="name">Glen R. Castellano</p><p class="title">President</p></div>
    </div>
    <ul class="contacts">
      <li><svg viewBox="0 0 10 10"><path d="M2 1h2l1 2-1 1a5 5 0 0 0 2 2l1-1 2 1v2a1 1 0 0 1-1 1A8 8 0 0 1 1 2a1 1 0 0 1 1-1z" fill="var(--green)"/></svg>(555) 555-0142</li>
      <li><svg viewBox="0 0 10 10"><rect x="0.5" y="2" width="9" height="6" fill="none" stroke="var(--green)"/><path d="M.5 2 5 5.5 9.5 2" fill="none" stroke="var(--green)"/></svg>glen@zuvadentalconsulting.example</li>
      <li><svg viewBox="0 0 10 10"><circle cx="5" cy="5" r="4.2" fill="none" stroke="var(--green)"/><path d="M1 5h8M5 .8c2 2.5 2 5.9 0 8.4M5 .8c-2 2.5-2 5.9 0 8.4" fill="none" stroke="var(--green)" stroke-width=".8"/></svg>www.zuvadentalconsulting.example</li>
    </ul>
    <div class="stripes"></div>
    <div class="foot-band">4817 W. Harborview Ave. &nbsp;|&nbsp; Larkspur Bay, KV</div>
  </section>

  <section class="sheet card card-back-light" aria-label="Business card back">
    <div class="centre">
      <div class="brand"><span class="brand-dot"></span>ZuvaDental</div>
      <p class="tagline">Marketing | Media | Management</p>
    </div>
    <div class="stripes"></div>
  </section>

  <section class="sheet card card-back-dark" aria-label="Business card back, dark">
    <div class="centre">
      <div class="brand brand--light"><span class="brand-dot"></span>ZuvaDental</div>
      <p class="tagline">Marketing | Media | Management</p>
    </div>
  </section>

</main>
</body>
</html>
```